Menu Design for Indian Restaurant

We are a new Indian restaurant, named Saffron Lantern Restaurant, looking for a sophisticated looking menu. It is a semi-formal dining restaurant with wooden tables and chairs and will have a focus on a creating a lively atmosphere. Environment-friendly products will be used, and the menu will be 100% vegetarian. There will be an emphasis on fresh, healthy and delicious food. We will be targeting vegans, vegetarians, health conscious people, people from all age groups, Indians, Australian's as well as other ethnic communities. We need a clean, simple, sophisticated design for the new restaurant menu. Attached is the restaurant logo for reference.

UPDATE:
- We have attached the menu
- We are not looking for any particular type of layout or size (open to suggests). Please suggest this after having a look at the menu contents. However, we will be having one formal menu to be used in the restaurant, and one in brochure form for distribution.
- There are no images at present. If you feel the need of images, please use sample images for now.

Thank you for the entries thus far.
Updates

Target Market(s)

All age groups from different nationalities

Industry/Entity Type

Indian Restaurant

Colors

Designer to choose colors to be used in the design.

Requirements
Nice to have
• This will be printed on environmentally friendly paper.

```html
<!DOCTYPE html>
<html lang="en">
<head>
<meta charset="utf-8">
<title>Saffron Lantern Restaurant – Menu Pages 4 and 5</title>
<link rel="stylesheet" href="https://fonts.googleapis.com/css2?family=Arimo:wght@700&family=Cabin:wght@400;500&family=Exo+2:ital,wght@1,800&display=swap">
<style>
  :root{
    --saffron:#f28a35;
    --saffron-soft:#f7a46a;
    --saffron-text:#d98432;
    --green:#17a65a;
    --green-deep:#17873f;
    --green-soft:#6fcf9a;
    --ink:#231f20;
    --ribbon-dark:#2b2b2b;
    --paper:#ffffff;
  }
  html,body{margin:0;padding:0;width:1200px;height:1158px;overflow:hidden;background:var(--paper);}
  .stage{position:relative;width:1500px;height:1448px;transform:scale(0.8);transform-origin:0 0;}
  .page{position:absolute;top:0;width:727px;height:1398px;overflow:hidden;
    background:linear-gradient(to bottom,var(--saffron-soft) 0,#fbd3b5 260px,#fff 380px,#fff 1080px,#d3f0df 1180px,var(--green-soft) 1398px);
    box-shadow:0 0 0 1px #9a9a9a;}
  .page--four{left:0;}
  .page--five{left:773px;}
  .pattern-band{position:absolute;left:0;top:0;width:727px;height:380px;
    background:linear-gradient(to bottom,rgba(246,150,90,.55),rgba(255,255,255,0));}
  .arch{position:absolute;left:0;top:0;width:727px;height:1398px;}
  .brand-name{position:absolute;left:150px;top:280px;width:427px;margin:0;text-align:center;
    font:500 40px/52px "Cabin",sans-serif;color:var(--green-deep);}
  .ribbon{position:absolute;left:73px;width:360px;height:46px;}
  .ribbon svg{position:absolute;left:0;top:0;}
  .ribbon-title{position:absolute;left:40px;top:3px;margin:0;font:italic 800 26px/40px "Exo 2",sans-serif;color:#fff;letter-spacing:.3px;white-space:nowrap;}
  .note{position:absolute;left:73px;margin:0;font:italic 800 17px/22px "Exo 2",sans-serif;color:var(--saffron);}
  .item{position:absolute;left:73px;right:60px;}
  .page--five .item{right:73px;}
  .item-name{margin:0;font:400 21px/24px "Cabin",sans-serif;color:var(--ink);}
  .price{position:absolute;right:0;top:2px;font:400 20px/24px "Cabin",sans-serif;color:var(--ink);}
  .item-desc{margin:1px 0 0;width:487px;font:500 15.5px/20px "Cabin",sans-serif;color:var(--saffron-text);}
  .item-desc--just{text-align:justify;text-align-last:left;}
  .item-desc--spaced{line-height:31px;width:455px;}
  .page-label{position:absolute;top:1412px;width:727px;margin:0;text-align:center;font:700 38px/40px "Arimo",sans-serif;color:#2b2b2b;}
  .page-label--four{left:0;}
  .page-label--five{left:773px;}
</style>
</head>
<body>
<main class="stage">

  <section class="page page--four" aria-label="Menu page 4">
    <div class="pattern-band" role="img" aria-label="Floral paisley pattern in saffron tones"></div>
    <svg class="arch" viewBox="0 0 727 1398" aria-hidden="true">
      <path fill="#fff" d="M40,1358 L40,478 C60,470 75,445 70,420 C65,395 28,385 25,350 C25,290 80,240 150,235 C200,230 230,200 240,170 C260,130 330,120 363,80 C396,120 466,130 486,170 C496,200 526,230 576,235 C646,240 700,290 700,350 C697,385 660,395 655,420 C650,445 665,470 688,478 L688,1358 Z"/>
      <path fill="none" stroke="var(--saffron)" stroke-width="5" d="M40,865 L40,478 C60,470 75,445 70,420 C65,395 28,385 25,350 C25,290 80,240 150,235 C200,230 230,200 240,170 C260,130 330,120 363,80 C396,120 466,130 486,170 C496,200 526,230 576,235 C646,240 700,290 700,350 C697,385 660,395 655,420 C650,445 665,470 688,478 L688,675"/>
      <path fill="none" stroke="var(--green)" stroke-width="5" d="M40,893 L40,1358 L688,1358 L688,703"/>
    </svg>
    <p class="brand-name">Saffron Lantern Restaurant</p>

    <div class="ribbon" style="top:492px">
      <svg width="360" height="46" viewBox="0 0 360 46" aria-hidden="true">
        <rect x="4" y="6" width="346" height="37" fill="#bdbdbd" opacity=".6"/>
        <rect x="0" y="1" width="340" height="37" fill="var(--saffron)"/>
        <polygon points="0,1 22,19.5 0,38" fill="var(--ribbon-dark)"/>
        <polygon points="336,1 356,19.5 336,38" fill="var(--ribbon-dark)"/>
      </svg>
      <h2 class="ribbon-title">SOUP OF THE DAY</h2>
    </div>
    <div class="item" style="top:538px"><h3 class="item-name">Cream of tomato with crotons</h3><span class="price">4.9</span></div>
    <div class="item" style="top:572px"><h3 class="item-name">Curried pumpkin with shallots</h3><span class="price">4.9</span></div>

    <div class="ribbon" style="top:607px">
      <svg width="360" height="46" viewBox="0 0 360 46" aria-hidden="true">
        <rect x="4" y="6" width="346" height="37" fill="#bdbdbd" opacity=".6"/>
        <rect x="0" y="1" width="340" height="37" fill="var(--saffron)"/>
        <polygon points="0,1 22,19.5 0,38" fill="var(--ribbon-dark)"/>
        <polygon points="336,1 356,19.5 336,38" fill="var(--ribbon-dark)"/>
      </svg>
      <h2 class="ribbon-title">ENTRÉE (TAPAS)</h2>
    </div>

    <div class="item" style="top:662px"><h3 class="item-name">Kamal Kofta (4pcs)</h3><span class="price">6.9</span>
      <p class="item-desc item-desc--just">Crispy potatoes curry leaves lotus stem ginger fresh coriander fresh chilli spice croquets</p></div>
    <div class="item" style="top:733px"><h3 class="item-name">Hara Kebab (4pcs)</h3><span class="price">6.9</span>
      <p class="item-desc item-desc--just">Fresh baby spinach ricotta cheese mash potatoes ginger fresh coriander fresh chilli patty</p></div>
    <div class="item" style="top:803px"><h3 class="item-name">Tandoori Fool (5pcs)</h3><span class="price">6.9</span>
      <p class="item-desc item-desc--just">Crispy tangy piquant mustard flavoured cheddar ginger garlic cauliflower and broccoli</p></div>
    <div class="item" style="top:874px"><h3 class="item-name">Tandoori Mushrooms (4pcs)</h3><span class="price">7.9</span>
      <p class="item-desc item-desc--just">Cup mushroom yogurt spice cheese fresh mint coriander onion capsicum</p></div>
    <div class="item" style="top:945px"><h3 class="item-name">Momos (6pcs)</h3><span class="price">6.9</span>
      <p class="item-desc">Vegetable stuffed pastry steamed serve with homemade chilli sauce</p></div>
    <div class="item" style="top:995px"><h3 class="item-name">Tandoori Momos (6pcs)</h3><span class="price">7.9</span>
      <p class="item-desc">Vegetable momos, yoghurt, ginger, garlic cooked in clay oven</p></div>
    <div class="item" style="top:1046px"><h3 class="item-name">Mushrooms Momos (6pcs)</h3><span class="price">6.9</span>
      <p class="item-desc">Pastry stuffed with mushrooms, steamed homemade chilli sauce</p></div>
    <div class="item" style="top:1096px"><h3 class="item-name">Paneer Tikka (4pcs)</h3><span class="price">7.9</span>
      <p class="item-desc">Cottage cheese gram flour mint chilli flavoured yogurt</p></div>
    <div class="item" style="top:1147px"><h3 class="item-name">Kabuli Tiki (4pcs)</h3><span class="price">6.9</span>
      <p class="item-desc">Chickpeas mince raw mango powder green sultana</p></div>
    <div class="item" style="top:1197px"><h3 class="item-name">Samosa Chat (2pcs)</h3><span class="price">6.9</span>
      <p class="item-desc">Crispy pastry stuffed potatoes peas on chickpeas</p></div>
    <div class="item" style="top:1248px"><h3 class="item-name">Aloo Tikki Chat (2pcs)</h3><span class="price">6.9</span>
      <p class="item-desc">Potato patty fresh coriander cumin seed pea flour on chickpeas</p></div>
    <div class="item" style="top:1298px"><h3 class="item-name">Dhai Bhalla Papdi</h3><span class="price">6.9</span>
      <p class="item-desc">Crispy pastry lentil dumpling yogurt date and mint chutney</p></div>
  </section>

  <section class="page page--five" aria-label="Menu page 5">
    <div class="pattern-band" role="img" aria-label="Floral paisley pattern in saffron tones"></div>
    <svg class="arch" viewBox="0 0 727 1398" aria-hidden="true">
      <path fill="#fff" d="M40,1358 L40,478 C60,470 75,445 70,420 C65,395 28,385 25,350 C25,290 80,240 150,235 C200,230 230,200 240,170 C260,130 330,120 363,80 C396,120 466,130 486,170 C496,200 526,230 576,235 C646,240 700,290 700,350 C697,385 660,395 655,420 C650,445 665,470 688,478 L688,1358 Z"/>
      <path fill="none" stroke="var(--saffron)" stroke-width="5" d="M40,865 L40,478 C60,470 75,445 70,420 C65,395 28,385 25,350 C25,290 80,240 150,235 C200,230 230,200 240,170 C260,130 330,120 363,80 C396,120 466,130 486,170 C496,200 526,230 576,235 C646,240 700,290 700,350 C697,385 660,395 655,420 C650,445 665,470 688,478 L688,675"/>
      <path fill="none" stroke="var(--green)" stroke-width="5" d="M40,893 L40,1358 L688,1358 L688,703"/>
    </svg>
    <p class="brand-name">Saffron Lantern Restaurant</p>

    <div class="ribbon" style="top:492px">
      <svg width="360" height="46" viewBox="0 0 360 46" aria-hidden="true">
        <rect x="4" y="6" width="346" height="37" fill="#bdbdbd" opacity=".6"/>
        <rect x="0" y="1" width="340" height="37" fill="var(--saffron)"/>
        <polygon points="0,1 22,19.5 0,38" fill="var(--ribbon-dark)"/>
        <polygon points="336,1 356,19.5 336,38" fill="var(--ribbon-dark)"/>
      </svg>
      <h2 class="ribbon-title">BURGER PARADE</h2>
    </div>
    <p class="note" style="top:542px">served with spicy potatoes fries</p>

    <div class="item" style="top:584px"><h3 class="item-name">Grass Hopper</h3><span class="price">7.9</span>
      <p class="item-desc item-desc--spaced" style="margin-top:2px">Vegetables potatoes patty beetroot carrot onion lettuce</p></div>
    <div class="item" style="top:648px"><h3 class="item-name">Cheese Hopper</h3><span class="price">7.9</span>
      <p class="item-desc item-desc--spaced" style="margin-top:3px">Potato cottage cheese patty tomato capsicum cucumber lettuce cheese</p></div>

    <div class="ribbon" style="top:774px">
      <svg width="360" height="46" viewBox="0 0 360 46" aria-hidden="true">
        <rect x="4" y="6" width="346" height="37" fill="#bdbdbd" opacity=".6"/>
        <rect x="0" y="1" width="340" height="37" fill="var(--saffron)"/>
        <polygon points="0,1 22,19.5 0,38" fill="var(--ribbon-dark)"/>
        <polygon points="336,1 356,19.5 336,38" fill="var(--ribbon-dark)"/>
      </svg>
      <h2 class="ribbon-title">PIZZA</h2>
    </div>
    <p class="note" style="top:819px">medium size</p>

    <div class="item" style="top:872px"><h3 class="item-name">Tropicana</h3><span class="price">11.9</span>
      <p class="item-desc" style="width:520px;margin-top:4px">Pineapple capsicum marjoram pitted black olive tomato cheese</p></div>
    <div class="item" style="top:935px"><h3 class="item-name">Mexicana</h3><span class="price" style="top:6px">12.9</span>
      <p class="item-desc" style="width:520px;margin-top:9px">Jalapeño capsicum tomato mushrooms black olive cheese</p></div>
    <div class="item" style="top:1003px"><h3 class="item-name">Kalamata</h3><span class="price" style="top:6px">12.9</span>
      <p class="item-desc" style="width:520px;margin-top:9px">Greek cheese capsicum red Kalamata olives onion tomato cheese</p></div>
    <div class="item" style="top:1071px"><h3 class="item-name">Siciliana</h3><span class="price" style="top:6px">12.9</span>
      <p class="item-desc" style="width:520px;margin-top:9px">Sun dry tomato green olive artichoke fresh parsley cheese</p></div>
    <div class="item" style="top:1139px"><h3 class="item-name">Indiana</h3><span class="price" style="top:6px">12.9</span>
      <p class="item-desc" style="width:520px;margin-top:9px">Cottage cheese tomato capsicum onion cheese</p></div>

    <div class="ribbon" style="top:1224px">
      <svg width="360" height="46" viewBox="0 0 360 46" aria-hidden="true">
        <rect x="4" y="6" width="346" height="37" fill="#bdbdbd" opacity=".6"/>
        <rect x="0" y="1" width="340" height="37" fill="var(--saffron)"/>
        <polygon points="0,1 22,19.5 0,38" fill="var(--ribbon-dark)"/>
        <polygon points="336,1 356,19.5 336,38" fill="var(--ribbon-dark)"/>
      </svg>
      <h2 class="ribbon-title">ALL TIME FAVOURITE</h2>
    </div>

    <div class="item" style="top:1285px"><h3 class="item-name">Channa Bhatura (2pcs)</h3><span class="price">9.9</span>
      <p class="item-desc" style="width:540px;margin-top:7px">Chickpeas onion tomato ginger fresh coriander deep fried bread pickle</p></div>
  </section>

  <p class="page-label page-label--four">PAGE 4</p>
  <p class="page-label page-label--five">PAGE 5</p>

</main>
</body>
</html>
```